Harbrook Builders PowerPoint Presentation

We need a sales pitch in powerpoint form for a "commercial only" construction company based out of Dallas, TX. We perform commercial only construction including ground up, build to suit, white box and many others. We would like the design to match the color scheme and outlook of the website and brochure that will be attached. Also, attached you will find the old presentation we used (it's terrible). http://www.harbrookbld.example/

Target Market(s)

Commercial property managers, commercial building owners, business owners, facility managers, commercial construction managers, construction design teams

Industry/Entity Type

Construction

Requirements
Must have
• Commercial construction pictures. Company overview. Specific industries served.
Should not have
• Residential pictures. Poor quality pictures. Anything that doesn't look like the website or attached brochure.

```html
<!DOCTYPE html>
<html lang="en">
<head>
<meta charset="utf-8">
<title>Harbrook Builders – Presentation Slides</title>
<link href="https://fonts.googleapis.com/css2?family=Montserrat:wght@500;600;700&family=Lato:wght@400;700&display=swap" rel="stylesheet">
<style>
  :root{
    --rust:#a9461a;
    --ink:#333333;
    --muted:#8a8a8a;
    --page:#ffffff;
    --edge:#e4e4e4;
  }
  *{box-sizing:border-box;margin:0;padding:0}
  html,body{width:1200px;height:2560px;overflow:hidden;background:var(--page)}
  body{position:relative;font-family:'Lato',Arial,sans-serif;color:var(--muted)}
  .slide{position:absolute;left:84px;width:1030px;height:580px;background:#fff;overflow:hidden;
    border:1px solid var(--edge);box-shadow:3px 4px 8px rgba(0,0,0,.35)}
  .abs{position:absolute}
  .heading{font-family:'Montserrat',Arial,sans-serif;font-weight:600;color:var(--rust);text-transform:uppercase}
  .label{font-family:'Montserrat',Arial,sans-serif;font-weight:500;color:var(--rust);text-transform:uppercase;font-size:12.5px;text-align:center}
  .note{font-size:10.5px;line-height:1.4;color:#999;text-align:center}
  .body{font-size:12px;line-height:1.5;color:#8f8f8f}
  .page-num{font-size:11px;color:#aaa}
  .brand{display:flex;align-items:center;gap:6px;font-family:'Montserrat',Arial,sans-serif;font-weight:700;font-size:15px;color:#222;letter-spacing:.2px}
  .brand-dot{width:14px;height:14px;border-radius:50%;background:var(--rust)}
  .icon{stroke:#222;stroke-width:1.6;fill:none;stroke-linecap:round;stroke-linejoin:round}
  .ring{position:absolute;width:84px;height:84px;border:4px solid var(--rust);border-radius:50%;display:flex;align-items:center;justify-content:center;background:#fff}
  .ring svg{width:38px;height:38px}
  .photo{position:absolute}
  .feature{position:absolute;width:170px;text-align:center}
  .feature svg{width:34px;height:34px;display:block;margin:0 auto 10px}
  .feature .label{margin-bottom:6px}
  /* slide 1 */
  .s1{top:56px}
  .s1 .photo{left:391px;top:0;width:639px;height:580px;background:linear-gradient(120deg,#e9eaec 0%,#c9ccd2 40%,#7f8da6 70%,#3a4256 100%)}
  /* slide 2 */
  .s2{top:678px}
  .s2 .photo{left:0;top:355px;width:1030px;height:225px;background:linear-gradient(90deg,#b9b6b4 0%,#dcdcdf 35%,#cfd2d8 65%,#9ea4ac 100%)}
  .tool{position:absolute;width:84px;text-align:center}
  .tool .label{position:absolute;top:94px;left:-10px;width:104px;font-weight:600;font-size:13px;line-height:1.3}
  /* slide 3 */
  .s3{top:1297px}
  .cell{position:absolute;width:343px;height:290px}
  .cell.text{text-align:center}
  .cell.text .ring{left:131px}
  .cell.text .label{font-size:14px;font-weight:600}
  .cell.text .note{width:235px;margin:0 auto;font-size:10.5px}
  /* slide 4 */
  .s4{top:1919px}
  .step{position:absolute;width:140px;text-align:center}
  .step .label{font-size:11.5px;margin-bottom:6px}
</style>
</head>
<body>

<!-- Slide: Standard overview -->
<section class="slide s1">
  <h2 class="heading abs" style="left:36px;top:34px;font-size:25px;letter-spacing:.3px">The Standard Lorem</h2>
  <p class="abs" style="left:36px;top:74px;width:340px;font-size:15px;line-height:1.35;color:#999;text-align:center">Lorem ipsum dolor sit amet, consectetuer adipiscing elit. Aenean commodo ligula eget dolor.</p>

  <div class="feature" style="left:21px;top:220px">
    <svg viewBox="0 0 24 24" class="icon"><path d="M6 22V4M6 4h14M6 8l4-4M10 4v3M18 4v5M16 9h4v3h-4zM3 22h7"/></svg>
    <div class="label">Lorem ipsum dolor</div>
    <p class="note">Aenean commodo ligula eget dolor. Aenean massa. Cum sociis natoque penatibus.</p>
  </div>
  <div class="feature" style="left:197px;top:220px">
    <svg viewBox="0 0 24 24" class="icon"><path d="M3 21V11l5 3v-3l5 3v-3l5 3V4h3v17zM6 17h2M11 17h2M16 17h2"/></svg>
    <div class="label">Lorem ipsum dolor</div>
    <p class="note">Aenean commodo ligula eget dolor. Aenean massa. Cum sociis natoque penatibus.</p>
  </div>
  <div class="feature" style="left:21px;top:362px">
    <svg viewBox="0 0 24 24" class="icon"><path d="M2 16V8h12v8M14 11h4l3 3v2H2M7 8l2-3h5"/><circle cx="6" cy="18" r="2"/><circle cx="17" cy="18" r="2"/></svg>
    <div class="label">Lorem ipsum dolor</div>
    <p class="note">Aenean commodo ligula eget dolor. Aenean massa. Cum sociis natoque penatibus.</p>
  </div>
  <div class="feature" style="left:197px;top:362px">
    <svg viewBox="0 0 24 24" class="icon"><path d="M4 15V9h7l2 6M13 15l3-9 4 3-2 6M1 18l3 2M4 15h16a2.5 2.5 0 0 1 0 5H4a2.5 2.5 0 0 1 0-5"/></svg>
    <div class="label">Lorem ipsum dolor</div>
    <p class="note">Aenean commodo ligula eget dolor. Aenean massa. Cum sociis natoque penatibus.</p>
  </div>

  <span class="page-num abs" style="left:48px;top:550px">8</span>
  <div class="brand abs" style="left:225px;top:545px"><span class="brand-dot"></span>Harbrook Builders</div>
  <div class="photo" role="img" aria-label="Photo of a site engineer in a hard hat and a manager reviewing building plans in an office"></div>
</section>

<!-- Slide: Services intro -->
<section class="slide s2">
  <div class="brand abs" style="right:30px;top:22px"><span class="brand-dot"></span>Harbrook Builders</div>
  <h2 class="heading abs" style="left:54px;top:100px;width:470px;font-size:23px;line-height:1.3;font-weight:700">Neque porro quisquam est qui dolorem ipsum quia dolor sit amet</h2>
  <p class="body abs" style="left:54px;top:200px;width:440px;font-size:11.5px">Lorem ipsum dolor sit amet, consectetur adipiscing elit, sed do eiusmod tempor incididunt ut labore et dolore magna aliqua. Ut enim ad minim veniam, quis nostrud exercitation ullamco laboris nisi ut aliquip ex ea commodo consequat. Duis aute irure dolor in reprehenderit in voluptate velit esse cillum dolore eu fugiat nulla pariatur. Excepteur sint occaecat</p>

  <div class="tool" style="left:610px;top:172px">
    <div class="ring" style="position:relative"><svg viewBox="0 0 24 24" class="icon"><rect x="5" y="3" width="13" height="5" rx="1"/><path d="M18 5h2v6h-8v3M11 14h2v7h-2z"/></svg></div>
    <div class="label">Lorem ipsum</div>
  </div>
  <div class="tool" style="left:730px;top:172px">
    <div class="ring" style="position:relative"><svg viewBox="0 0 24 24" class="icon"><path d="M3 7h12v6H3zM15 9h3M19 10h3M7 13l-1 8h4l1-8"/></svg></div>
    <div class="label">Lorem ipsum</div>
  </div>
  <div class="tool" style="left:850px;top:172px">
    <div class="ring" style="position:relative"><svg viewBox="0 0 24 24" class="icon"><path d="M4 14a8 8 0 0 1 16 0M2 14h20v2H2zM10 6v4M14 6v4M7 18h4v2H7zM13 18h4v2h-4z"/></svg></div>
    <div class="label">Lorem ipsum</div>
  </div>

  <div class="photo" role="img" aria-label="Photo of architectural blueprints with a tape measure, hard hat, pens and a calculator on a desk"></div>
</section>

<!-- Slide: Service grid -->
<section class="slide s3">
  <div class="cell photo" style="left:0;top:0;background:linear-gradient(135deg,#9fb7c0,#d9c6b0 55%,#b39a88)" role="img" aria-label="Photo of a smiling builder in a red hard hat giving a thumbs up"></div>
  <div class="cell text" style="left:343px;top:0">
    <div class="ring" style="top:28px"><svg viewBox="0 0 24 24" class="icon"><path d="M2 5h3l3 10h9l3-7H7"/><circle cx="10" cy="19" r="1.6"/><circle cx="16" cy="19" r="1.6"/></svg></div>
    <div style="padding-top:124px">
      <div class="label" style="margin-bottom:6px">Lorem ipsum</div>
      <p class="note">Lorem ipsum dolor sit amet, consectetur adipiscing elit, sed do eiusmod tempor incididunt ut labore et dolore magna aliqua. Ut enim ad minim veniam, quis nostrud exercitation ullamco</p>
    </div>
  </div>
  <div class="cell photo" style="left:686px;top:0;background:linear-gradient(120deg,#c8a790,#c6c3c0 50%,#6f7f95)" role="img" aria-label="Photo of a worker in a white hard hat and safety glasses at a wall"></div>

  <div class="cell text" style="left:0;top:290px">
    <div class="ring" style="top:38px"><svg viewBox="0 0 24 24" class="icon"><path d="M3 5h18v14H3zM3 9.7h18M3 14.3h18M9 5v4.7M15 5v4.7M6 9.7v4.6M12 9.7v4.6M18 9.7v4.6M9 14.3V19M15 14.3V19"/></svg></div>
    <div style="padding-top:134px">
      <div class="label" style="margin-bottom:6px">Lorem ipsum</div>
      <p class="note">Lorem ipsum dolor sit amet, consectetur adipiscing elit, sed do eiusmod tempor incididunt ut labore et dolore magna aliqua. Ut enim ad minim veniam, quis nostrud exercitation ullamco</p>
    </div>
  </div>
  <div class="cell photo" style="left:343px;top:290px;background:linear-gradient(160deg,#e2c53c 0%,#dcdcda 35%,#cfd0d2 100%)" role="img" aria-label="Photo of a yellow hard hat resting on building blueprints"></div>
  <div class="cell text" style="left:686px;top:290px">
    <div class="ring" style="top:38px"><svg viewBox="0 0 24 24" class="icon"><path d="M3 15h11v-4h-7l-2 4M14 12l4-6 3 3-2 2M4 18h12a1.5 1.5 0 0 1 0 3H4a1.5 1.5 0 0 1 0-3"/></svg></div>
    <div style="padding-top:134px">
      <div class="label" style="margin-bottom:6px">Lorem ipsum</div>
      <p class="note">Lorem ipsum dolor sit amet, consectetur adipiscing elit, sed do eiusmod tempor incididunt ut labore et dolore magna aliqua. Ut enim ad minim veniam, quis nostrud exercitation ullamco</p>
    </div>
  </div>
  <span class="page-num abs" style="right:52px;top:552px">13</span>
</section>

<!-- Slide: Process timeline -->
<section class="slide s4">
  <h2 class="heading abs" style="left:0;width:1030px;top:70px;text-align:center;font-size:24px;font-weight:600">Lorem ipsum dolor sit amet, consectetur adipiscing elit</h2>
  <p class="body abs" style="left:82px;width:866px;top:112px;text-align:center;font-size:11.5px;line-height:1.45">At vero eos et accusamus et iusto odio dignissimos ducimus qui blanditiis praesentium voluptatum deleniti atque corrupti quos dolores et quas molestias excepturi sint occaecati cupiditate non provident, similique sunt in culpa qui officia deserunt mollitia animi, id est laborum et dolorum fuga. Et harum quidem rerum facilis est et expedita distinctio. Nam libero tempore, cum soluta nobis est eligendi optio cumque nihil impedit quo minus id quod.</p>

  <svg class="abs" style="left:0;top:290px" width="1030" height="120" viewBox="0 0 1030 120">
    <g fill="var(--rust)">
      <rect x="200" y="48" width="560" height="24"/>
      <circle cx="210" cy="60" r="56"/>
      <circle cx="400" cy="60" r="56"/>
      <circle cx="590" cy="60" r="56"/>
      <circle cx="780" cy="60" r="56"/>
    </g>
    <g fill="#fff">
      <circle cx="210" cy="60" r="37"/>
      <circle cx="400" cy="60" r="37"/>
      <circle cx="590" cy="60" r="37"/>
      <circle cx="780" cy="60" r="37"/>
    </g>
    <g class="icon" transform="translate(194 44) scale(1.35)"><rect x="5" y="3" width="13" height="5" rx="1"/><path d="M18 5h2v6h-8v3M11 14h2v7h-2z"/></g>
    <g class="icon" transform="translate(384 44) scale(1.35)"><path d="M3 7h12v6H3zM15 9h3M19 10h3M7 13l-1 8h4l1-8"/></g>
    <g class="icon" transform="translate(574 44) scale(1.35)"><path d="M4 14a8 8 0 0 1 16 0M2 14h20v2H2zM10 6v4M14 6v4M7 18h4v2H7zM13 18h4v2h-4z"/></g>
    <g class="icon" transform="translate(764 44) scale(1.35)"><path d="M2 5h3l3 10h9l3-7H7"/><circle cx="10" cy="19" r="1.6"/><circle cx="16" cy="19" r="1.6"/></g>
  </svg>

  <div class="step" style="left:330px;top:222px">
    <div class="label">Lorem ipsum dolor</div>
    <p class="note">Aenean commodo ligula eget dolor. Aenean massa. Cum sociis natoque penatibus.</p>
  </div>
  <div class="step" style="left:710px;top:222px">
    <div class="label">Lorem ipsum dolor</div>
    <p class="note">Aenean commodo ligula eget dolor. Aenean massa. Cum sociis natoque penatibus.</p>
  </div>
  <div class="step" style="left:140px;top:432px">
    <div class="label">Lorem ipsum dolor</div>
    <p class="note">Aenean commodo ligula eget dolor. Aenean massa. Cum sociis natoque penatibus.</p>
  </div>
  <div class="step" style="left:520px;top:432px">
    <div class="label">Lorem ipsum dolor</div>
    <p class="note">Aenean commodo ligula eget dolor. Aenean massa. Cum sociis natoque penatibus.</p>
  </div>
  <span class="page-num abs" style="right:52px;top:552px">31</span>
</section>

</body>
</html>
```